GLP letterhead

We need a letterhead design for our new company based in Los Angeles called "Gold Lantern Pictures". We develop film and television projects. We work with investors, financiers, film production companies, film distribution and sales companies as well as studios. We would like to incorporate our logo (see attached) but make the letterhead simple and elegant. We need to include: logo, company address, phone number and company website.
Updates

Hello designers, Thanks for your submissions. For our letterhead, we are looking for something more simple and elegant. No heavy bars or lines. Make it feel light and clean. Not a lot of ink on the page. Use the logo and contact info but think "clean", "streamlined" and mostly white paper. Looking forward to seeing more... thanks! Gold Lantern Pictures team

Target Market(s)

Studio executives, talent agents and agencies, financiers, investors.

Industry/Entity Type

It Company

Requirements
Must have
• Gold Lantern Pictures logo (see attached). Logo may be cropped and altered appropriately for elegant letterhead design.
• Please include:
• COMPANY ADDRESS:
• Ridgeway Studio Park
• 2850 Halverson Street
• Tower Annex, 4th Floor
• Manhattan Beach, CA 90412
• COMPANY WEBSITE:
• www.goldlanternpicturesco.example
• COMPANY PHONE NUMBER:
• 310-555-0148

```html
<!DOCTYPE html>
<html lang="en">
<head>
<meta charset="utf-8">
<title>Gold Lantern Pictures — Letterhead</title>
<link rel="stylesheet" href="https://fonts.googleapis.com/css2?family=PT+Sans+Narrow:wght@400;700&display=swap">
<style>
  :root {
    --ink: #3b3b3b;
    --accent: #17c4df;
    --sidebar: #f7f8f9;
    --rule: #e4e6e8;
    --paper: #ffffff;
    --wave: #eceef0;
  }
  * { margin: 0; padding: 0; box-sizing: border-box; }
  html, body {
    width: 927px;
    height: 1200px;
    overflow: hidden;
    background: var(--paper);
  }
  .letterhead {
    position: relative;
    width: 927px;
    height: 1200px;
    background: var(--paper);
    font-family: "PT Sans Narrow", "Arial Narrow", sans-serif;
    color: var(--ink);
    overflow: hidden;
  }
  .sidebar {
    position: absolute;
    left: 0; top: 0;
    width: 174px;
    height: 1200px;
    background: var(--sidebar);
    border-right: 1px solid var(--rule);
  }
  .brand {
    position: absolute;
    left: 0; top: 66px;
    width: 174px;
    text-align: center;
  }
  .brand-mark { display: block; margin: 0 auto; }
  .brand-name {
    margin-top: 6px;
    font-size: 12px;
    font-weight: 400;
    letter-spacing: 0.9px;
    text-transform: uppercase;
    color: var(--accent);
  }
  .brand-tagline {
    margin-top: 2px;
    font-size: 5.5px;
    letter-spacing: 0.6px;
    text-transform: uppercase;
    color: var(--ink);
  }
  .wave-field {
    position: absolute;
    left: 175px; top: 720px;
    width: 752px; height: 480px;
    background:
      radial-gradient(ellipse 90% 70% at 85% 75%, rgba(236,238,240,0.8), rgba(236,238,240,0) 70%),
      linear-gradient(160deg, rgba(255,255,255,0) 45%, var(--wave) 100%);
  }
  .letter {
    position: absolute;
    left: 223px; top: 211px;
    width: 690px;
    font-size: 16.5px;
    letter-spacing: 0.5px;
    line-height: 21.9px;
    white-space: nowrap;
  }
  .letter-date {
    color: var(--accent);
    margin-bottom: 23px;
  }
  .letter p { margin-bottom: 22px; }
  .letter-closing {
    position: absolute;
    left: 223px; top: 932px;
    font-size: 16.5px;
    letter-spacing: 0.5px;
    line-height: 22px;
  }
  .letter-signature { margin-top: 43px; }
  .contact-line {
    position: absolute;
    left: 175px; top: 1150px;
    width: 752px;
    text-align: center;
    font-size: 10px;
    color: var(--accent);
    white-space: nowrap;
  }
  .contact-line .sep { margin: 0 9px; }
</style>
</head>
<body>
<main class="letterhead">
  <aside class="sidebar">
    <div class="brand">
      <svg class="brand-mark" width="74" height="74" viewBox="0 0 74 74" aria-hidden="true">
        <circle cx="37" cy="37" r="34" fill="#17c4df"/>
      </svg>
      <div class="brand-name">Gold Lantern Pictures</div>
      <div class="brand-tagline">A Media Entertainment Company</div>
    </div>
  </aside>

  <div class="wave-field" role="img" aria-label="Faint flowing line pattern in light grey"></div>

  <section class="letter">
    <div class="letter-date">September 21, 2014</div>
    <p>Proin gravida nibh vel velit auctor aliquet.</p>
    <p>Aenean sollicitudin, lorem quis bibendum auctor, nisi elit consequat ipsum, nec sagittis sem nibh id elit.<br>Duis sed odio sit amet nibh vulputate cursus a sit amet mauris. Morbi accumsan ipsum velit. Nam nec<br>tellus a odio tincidunt auctor a ornare odio. Sed non&nbsp; mauris vitae erat consequat auctor eu in elit. Class<br>aptent taciti sociosqu ad litora torquent per conubia nostra, per inceptos himenaeos. Mauris in erat justo.<br>Nullam ac urna eu felis dapibus condimentum sit amet a augue. Sed non neque elit. Sed ut imperdiet<br>nisi. Proin condimentum fermentum nunc. Etiam pharetra, erat sed fermentum feugiat, velit mauris<br>egestas quam, ut aliquam massa nisl quis neque. Suspendisse in orci enim.</p>
    <p>Proin gravida nibh vel velit auctor aliquet. Aenean sollicitudin, lorem quis bibendum auctor, nisi elit con-<br>sequat ipsum, nec sagittis sem nibh id elit. Duis sed odio sit amet nibh vulputate cursus a sit amet<br>mauris. Morbi accumsan ipsum velit. Nam nec tellus a odio tincidunt auctor a ornare odio. Sed non<br>mauris vitae erat consequat auctor eu in elit. Class aptent taciti sociosqu ad litora torquent per conubia<br>nostra, per inceptos himenaeos. Mauris in erat justo. Nullam ac urna eu felis dapibus condimentum sit<br>amet a augue. Sed non neque elit. Sed ut imperdiet nisi. Proin condimentum fermentum nunc. Etiam<br>pharetra, erat sed fermentum feugiat, velit mauris egestas quam, ut aliquam massa nisl quis neque.<br>Suspendisse in orci enim.</p>
    <p>Proin gravida nibh vel velit auctor aliquet. Aenean sollicitudin, lorem quis bibendum auctor, nisi elit con-<br>sequat ipsum, nec sagittis sem nibh id elit. Duis sed odio sit amet nibh vulputate cursus a sit amet<br>mauris. Morbi accumsan ipsum velit. Nam nec tellus a odio tincidunt auctor a ornare odio. Sed non<br>mauris vitae erat consequat auctor eu in elit. Class aptent taciti sociosqu ad litora torquent per conubia<br>nostra, per inceptos himenaeos. Mauris in erat justo. Nullam ac urna eu felis dapibus condimentum sit<br>amet a augue. Sed non neque elit. Sed ut imperdiet nisi. Proin condimentum fermentum nunc. Etiam<br>pharetra, erat sed fermentum feugiat, velit mauris egestas quam, ut aliquam massa nisl quis neque.<br>Suspendisse in orci enim.</p>
  </section>

  <div class="letter-closing">
    <div>Yours faithfully,</div>
    <div class="letter-signature">Gold Lantern Pictures Team</div>
  </div>

  <footer class="contact-line">
    Ridgeway Studio Park 2850 Halverson Street Tower Annex, 4th Floor&nbsp; Manhattan Beach, CA 90412<span class="sep">|</span>310-555-0148<span class="sep">|</span>www.goldlanternpicturesco.example
  </footer>
</main>
</body>
</html>
```